Business card website / business card for website

We are a French website selling products Made in USA of quality, we need a business card to give from hand to hand and for deposit in the cartons of Each order. We-have the logo That I send in the attachments The theme is: US Vintage and find the compromised entre les national park ambience us and the atmosphere Brooklyn If you can make the feeling it's great The site www.latablederivebleue.com (opening April) You can change the logo a little gold in color it could ... we are a French website selling products Made in USA quality, we need a business card to give from hand to hand and deposit in cartons each order. we have the logo that I convey in the attached parts is the theme: Vintage embiance US and find a compromise between the atmosphere us national park and the atmosphere Brooklyn at: www.latablederivebleue.com (opening April) if you can the impression is great

Target Market(s)

25-50 YEARS man, woman.

Industry/Entity Type

Business

Contact Information for Business Card

www.latablederivebleue.com
N'oubliez pas que nous sommes là si vous avez besoin de nouscontact@latablederivebleue.com

Font styles to use
Serif

Requirements
Must have
• my logo with "general store", my email address preceded by the phrase: Do not forget that we are here if you need us My logo with the words "general store," my email address Preceded by the sentence: remember we're here if you need us (in french)
Nice to have
• i like this style: http://designcorbel.net/ideas/print-ideas/25-charming-old-style-business-card-designs/ must feel the Vintage America it must feel the Vintage America lice can change a little logo or to color ... You can change the logo a little gold in color it could ... i like kraft paper with red ....
Should not have

```html
<!DOCTYPE html>
<html lang="fr">
<head>
<meta charset="utf-8">
<title>La Table de Rive Bleue — Carte de visite</title>
<link rel="stylesheet" href="https://fonts.googleapis.com/css2?family=Lora:ital,wght@0,400;0,600;1,400&display=swap">
<style>
  :root {
    --backdrop: #e9e6e1;
    --card-light: #ffffff;
    --card-dark: #2b2b2b;
    --ink: #333333;
    --ink-soft: #8c8c8c;
    --rule: #444444;
    --illustration-light: #cfcfcf;
    --illustration-dark: #6f6f6f;
    --on-dark: #ffffff;
  }
  * { margin: 0; padding: 0; box-sizing: border-box; }
  html, body {
    width: 1200px;
    height: 987px;
    overflow: hidden;
    background: var(--backdrop);
    font-family: "Lora", Georgia, serif;
    color: var(--ink);
  }
  .card {
    position: absolute;
    left: 293px;
    width: 615px;
    height: 352px;
    box-shadow: 0 3px 10px rgba(0,0,0,0.18);
  }
  .card--front { top: 130px; background: var(--card-light); }
  .card--back { top: 506px; height: 350px; background: var(--card-dark); }

  .brand-seal {
    position: absolute;
    left: 414px;
    top: 30px;
    width: 172px;
    height: 172px;
    border: 2px solid var(--ink);
    border-radius: 50%;
    display: flex;
    align-items: center;
    justify-content: center;
    text-align: center;
  }
  .brand-name {
    font-size: 15px;
    font-weight: 600;
    line-height: 1.3;
    color: var(--ink);
    letter-spacing: 0.5px;
    text-transform: uppercase;
  }

  .holder-name {
    position: absolute;
    left: 31px;
    top: 188px;
    font-size: 22px;
    font-weight: 600;
    letter-spacing: 0.3px;
  }
  .holder-role {
    position: absolute;
    left: 31px;
    top: 217px;
    font-size: 15px;
    color: var(--ink-soft);
  }
  .divider {
    position: absolute;
    left: 31px;
    top: 244px;
    width: 543px;
    height: 1px;
    background: var(--rule);
  }
  .contact-list {
    position: absolute;
    list-style: none;
    font-size: 15px;
    line-height: 23.5px;
  }
  .contact-list li { display: flex; align-items: center; gap: 7px; white-space: nowrap; }
  .contact-list svg { width: 14px; height: 14px; fill: var(--ink); flex: none; }
  .contact-list--phones { left: 31px; top: 257px; }
  .contact-list--online { right: 30px; top: 257px; text-align: right; }
  .contact-list--online li { justify-content: flex-end; }
  .contact-note { font-size: 13px; font-style: italic; color: var(--ink-soft); }

  .barn-illustration {
    position: absolute;
    left: 357px;
    top: 110px;
    width: 232px;
    height: 95px;
    background: linear-gradient(180deg, var(--illustration-light), var(--illustration-dark));
    opacity: 0.85;
  }
  .back-url {
    position: absolute;
    right: 30px;
    top: 308px;
    font-size: 15px;
    font-style: italic;
    color: var(--on-dark);
  }
</style>
</head>
<body>
  <section class="card card--front">
    <div class="brand-seal">
      <span class="brand-name">La Table de<br>Rive Bleue<br>General Store</span>
    </div>

    <h1 class="holder-name">LUCAS MOREAU</h1>
    <p class="holder-role">CEO/Founder</p>
    <div class="divider"></div>

    <ul class="contact-list contact-list--phones">
      <li>
        <svg viewBox="0 0 16 16" aria-hidden="true"><path d="M3.6 1.2l2.3 2.9-1.3 1.8c.8 1.8 2.3 3.3 4.1 4.2l1.8-1.4 2.9 2.2-1.2 2.6C6.9 13.2 2.5 8.8 1 3.5z"/></svg>
        612 408 3175
      </li>
      <li>
        <svg viewBox="0 0 16 16" aria-hidden="true"><path d="M4.5 0h7A1.5 1.5 0 0 1 13 1.5v13a1.5 1.5 0 0 1-1.5 1.5h-7A1.5 1.5 0 0 1 3 14.5v-13A1.5 1.5 0 0 1 4.5 0zM5 2v10h6V2zm3 11a1 1 0 1 0 0 2 1 1 0 0 0 0-2z"/></svg>
        617 552 9043
      </li>
      <li>
        <svg viewBox="0 0 16 16" aria-hidden="true"><path d="M4 1h8v4H4zM1 6h14v6h-2v3H3v-3H1zm4 5v3h6v-3z"/></svg>
        612 408 3176
      </li>
    </ul>

    <ul class="contact-list contact-list--online">
      <li class="contact-note">N'oubliez pas que nous sommes là si vous avez besoin de</li>
      <li>
        nouscontact@latablederivebleue.com
        <svg viewBox="0 0 16 16" aria-hidden="true"><path d="M1 3h14v10H1zm1.5 1.2L8 8.5l5.5-4.3z"/></svg>
      </li>
      <li>
        latablederivebleue.com
        <svg viewBox="0 0 16 16" aria-hidden="true"><path d="M8 1a7 7 0 1 0 0 14A7 7 0 0 0 8 1zm-1 2.2c-.6 1-2.5 1.3-2.2 2.8.3 1.2 2 .9 2.5 2.2.3 1-.7 1.8 0 3 .4.7 1 1.5.8 2.1A5.6 5.6 0 0 1 7 3.2zm3.5 1.3c.9.6 2.5 2 2.6 3.6-.8.2-1.6-.6-2.4-.1-.6.4-.4 1.4-1.2 1.5-.8.1-1.4-1-1-1.8.5-.9 1.8-1.3 2-3.2z"/></svg>
      </li>
    </ul>
  </section>

  <section class="card card--back">
    <div class="barn-illustration" role="img" aria-label="White line drawing of a gambrel-roofed wooden barn flanked by pine trees"></div>
    <p class="back-url">www.latablederivebleue.com</p>
  </section>
</body>
</html>
```